KIVO 248
I need double sided standard sized Business Card [3.5" x 2"]
Open to designers choice
Modern
Pavel Rudakovsky
PO BOX 7132
Downey, CA 90318
pavel@tumq4.com
kivo248.com

```html
<!DOCTYPE html>
<html lang="en">
<head>
<meta charset="utf-8">
<title>KIVO 248 Business Card</title>
<link rel="stylesheet" href="https://fonts.googleapis.com/css2?family=Open+Sans:ital,wght@0,400;0,600;0,700;1,400&display=swap">
<style>
  :root {
    --page: #e6e6e6;
    --card-black: #121212;
    --card-white: #ffffff;
    --orange-light: #f7b21e;
    --orange: #f07a12;
    --orange-deep: #c83a0c;
    --brand-red: #e2350f;
    --ink: #4a4a4a;
    --ink-soft: #6d6d6d;
    --arc-grey: #9a9a9a;
  }
  * { margin: 0; padding: 0; box-sizing: border-box; }
  html, body { width: 1200px; height: 901px; overflow: hidden; }
  body {
    background: var(--page);
    font-family: "Open Sans", Arial, sans-serif;
    position: relative;
  }
  .card {
    position: absolute;
    left: 250px;
    width: 700px;
    height: 400px;
    border-radius: 18px;
    overflow: hidden;
    box-shadow: 0 8px 24px rgba(0,0,0,0.25);
  }
  .card-back { top: 30px; background: var(--card-black); }
  .card-front { top: 471px; background: var(--card-white); }

  .back-mark {
    position: absolute;
    left: 0; right: 0; top: 140px;
    display: flex; align-items: center; justify-content: center; gap: 14px;
  }
  .brand-square {
    width: 56px; height: 56px; border-radius: 10px;
    background: linear-gradient(180deg, var(--orange-light), var(--orange-deep));
  }
  .brand-name {
    font-weight: 700;
    color: var(--brand-red);
    letter-spacing: 1px;
  }
  .card-back .brand-name { font-size: 40px; color: var(--orange); }
  .back-url {
    position: absolute; left: 0; right: 0; top: 222px;
    text-align: center; color: #8a8a8a; font-size: 16px; letter-spacing: 1px;
  }

  .front-art { position: absolute; inset: 0; }
  .front-mark {
    position: absolute; left: 36px; top: 110px;
    display: flex; align-items: center; gap: 14px;
  }
  .card-front .brand-square { width: 62px; height: 62px; }
  .card-front .brand-name { font-size: 44px; }
  .person {
    position: absolute; right: 60px; top: 62px; text-align: right; color: #fff;
  }
  .person-name { font-size: 21px; font-weight: 700; }
  .person-role { font-size: 13px; margin-top: 2px; }
  .address {
    position: absolute; left: 40px; top: 272px;
    color: var(--ink); font-size: 16px; font-style: italic; line-height: 1.35;
  }
  .contacts {
    position: absolute; left: 420px; top: 256px;
    list-style: none; color: var(--ink); font-size: 15px; line-height: 1.45;
  }
  .contacts li { display: flex; align-items: center; gap: 8px; }
  .contacts svg { width: 16px; height: 16px; flex: none; }
</style>
</head>
<body>

<section class="card card-back" aria-label="Card back">
  <div class="back-mark">
    <span class="brand-square"></span>
    <span class="brand-name">KIVO 248</span>
  </div>
  <p class="back-url">kivo248.com</p>
</section>

<section class="card card-front" aria-label="Card front">
  <svg class="front-art" viewBox="0 0 700 400" width="700" height="400" aria-hidden="true">
    <defs>
      <linearGradient id="swoosh" x1="0" y1="0" x2="1" y2="0.4">
        <stop offset="0" stop-color="var(--orange-light)"/>
        <stop offset="0.45" stop-color="var(--orange)"/>
        <stop offset="1" stop-color="var(--orange-deep)"/>
      </linearGradient>
    </defs>
    <path d="M150 0 L700 0 L700 400 L665 400 C700 260 650 160 530 110 C420 66 270 55 150 0 Z" fill="url(#swoosh)"/>
    <path d="M150 6 C270 62 420 76 524 120 C640 170 686 260 652 400" fill="none" stroke="var(--arc-grey)" stroke-width="4"/>
  </svg>

  <div class="front-mark">
    <span class="brand-square"></span>
    <span class="brand-name">KIVO 248</span>
  </div>

  <div class="person">
    <p class="person-name">Pavel Rudakovsky</p>
    <p class="person-role">CEO</p>
  </div>

  <address class="address">
    PO BOX 7132<br>
    Downey, CA 90318
  </address>

  <ul class="contacts">
    <li><svg viewBox="0 0 16 16"><path d="M3 2h3l1 3-2 1c1 2 2 3 4 4l1-2 3 1v3c0 1-1 2-2 2C6 14 2 10 1 4c0-1 1-2 2-2z" fill="var(--orange)"/></svg>8885550142</li>
    <li><svg viewBox="0 0 16 16"><rect x="2" y="5" width="12" height="8" rx="1" fill="var(--orange)"/><rect x="4" y="2" width="8" height="4" fill="var(--orange-deep)"/></svg>5625550187</li>
    <li><svg viewBox="0 0 16 16"><rect x="4" y="1" width="8" height="14" rx="2" fill="var(--orange)"/><rect x="6" y="3" width="4" height="7" fill="#fff"/></svg>8885550163</li>
    <li><svg viewBox="0 0 16 16"><rect x="1" y="3" width="14" height="10" rx="1" fill="var(--orange)"/><path d="M1 4l7 5 7-5" fill="none" stroke="#fff" stroke-width="1.4"/></svg>pavel@tumq4.com</li>
    <li><svg viewBox="0 0 16 16"><circle cx="8" cy="8" r="7" fill="var(--orange)"/><path d="M1 8h14M8 1c3 3 3 11 0 14M8 1c-3 3-3 11 0 14" fill="none" stroke="#fff" stroke-width="1"/></svg>kivo248.com</li>
  </ul>
</section>

</body>
</html>
```